brindle's business card for earthmoving and tipper hire business.

I have a small earthmoving and tipper truck company. I am aiming for the smaller jobs that the big guys don't want. I am also Doing grass slashing and fire hazard reduction work. I would like to see some earthy colors, greens browns etc. I have a tractor with a front end loader attachment, and a 22 ton tipper. I would like to maybe have a silhouette of a tipper and tractor/slasher/loader setup in centre with my business name over the top and details to one side or something like that

Industry/Entity Type

Business

Contact Information for Business Card

Brindle's small earthworks and tipper hireToowoombaABN: 47781050480PH 0479126773Email brindle.4@fenwickmail.com

Font styles to use
Sans Serif

Colors
fbee3d
abd036
85cae6
f78f20

Requirements
Nice to have
• Earthy colors . business name in blue

```html
<!DOCTYPE html>
<html lang="en">
<head>
<meta charset="utf-8">
<title>Brindle's small earthworks and tipper – business card</title>
<link rel="stylesheet" href="https://fonts.googleapis.com/css2?family=Didact+Gothic&family=Montserrat:wght@800&display=swap">
<style>
  :root {
    --backdrop: #e9e6e1;
    --slate: #3f4751;
    --slate-light: #58616b;
    --orange: #f78f20;
    --orange-deep: #f07a12;
    --ink: #2f343a;
    --paper: #ffffff;
    --mist: #d9dde1;
  }
  * { box-sizing: border-box; margin: 0; padding: 0; }
  html, body { width: 1200px; height: 900px; overflow: hidden; }
  body {
    background: var(--backdrop);
    font-family: "Didact Gothic", "Century Gothic", sans-serif;
    position: relative;
  }
  .card {
    position: absolute;
    width: 640px;
    height: 366px;
    border-radius: 4px;
    overflow: hidden;
    box-shadow: 0 10px 28px rgba(0,0,0,.22);
  }
  /* back of card */
  .card-back {
    left: 150px; top: 60px;
    background: linear-gradient(120deg, var(--slate) 0%, var(--slate-light) 60%, var(--slate) 100%);
  }
  .service-list {
    list-style: none;
    position: absolute; left: 40px; top: 34px;
    color: #e6e9ec; font-size: 19px; letter-spacing: .5px;
  }
  .service-list li { display: flex; align-items: center; gap: 10px; height: 30px; }
  .tick { width: 20px; height: 20px; flex: none; }
  .card-back .brand {
    position: absolute; right: 38px; bottom: 58px;
    text-align: right; color: var(--mist);
  }
  /* front of card */
  .card-front { left: 410px; top: 460px; background: var(--paper); }
  .swoosh { position: absolute; inset: 0; }
  .brand {
    font-family: "Montserrat", sans-serif; font-weight: 800;
    line-height: 1.05;
  }
  .brand-name { font-size: 36px; letter-spacing: -.5px; display: block; }
  .brand-line { font-size: 16px; display: block; margin-top: 4px; }
  .card-front .brand {
    position: absolute; left: 32px; top: 152px; color: var(--ink);
  }
  .contact { position: absolute; left: 346px; top: 38px; color: var(--ink); }
  .contact-name { font-size: 26px; letter-spacing: .5px; }
  .contact-title { font-size: 15px; color: var(--orange); margin-bottom: 6px; }
  .contact-row { display: flex; align-items: center; gap: 10px; font-size: 18px; height: 28px; }
  .contact-row svg { width: 15px; height: 15px; flex: none; }
  .contact-abn { font-size: 18px; margin-top: 4px; }
  .contact-abn span { color: var(--orange); }
</style>
</head>
<body>

<section class="card card-back" aria-label="Card back">
  <ul class="service-list">
    <li><svg class="tick" viewBox="0 0 20 20"><rect x="1.5" y="4.5" width="13" height="13" fill="none" stroke="var(--orange)" stroke-width="2"/><path d="M4 10l4 4 10-11" fill="none" stroke="var(--orange)" stroke-width="3"/></svg>Small Earthworks</li>
    <li><svg class="tick" viewBox="0 0 20 20"><rect x="1.5" y="4.5" width="13" height="13" fill="none" stroke="var(--orange)" stroke-width="2"/><path d="M4 10l4 4 10-11" fill="none" stroke="var(--orange)" stroke-width="3"/></svg>Slashing</li>
    <li><svg class="tick" viewBox="0 0 20 20"><rect x="1.5" y="4.5" width="13" height="13" fill="none" stroke="var(--orange)" stroke-width="2"/><path d="M4 10l4 4 10-11" fill="none" stroke="var(--orange)" stroke-width="3"/></svg>Fire Hazards Reduction</li>
    <li><svg class="tick" viewBox="0 0 20 20"><rect x="1.5" y="4.5" width="13" height="13" fill="none" stroke="var(--orange)" stroke-width="2"/><path d="M4 10l4 4 10-11" fill="none" stroke="var(--orange)" stroke-width="3"/></svg>Rural Clean-ups</li>
    <li><svg class="tick" viewBox="0 0 20 20"><rect x="1.5" y="4.5" width="13" height="13" fill="none" stroke="var(--orange)" stroke-width="2"/><path d="M4 10l4 4 10-11" fill="none" stroke="var(--orange)" stroke-width="3"/></svg>Tipper</li>
  </ul>
  <div class="brand">
    <span class="brand-name">Brindle's small</span>
    <span class="brand-line">earthworks and tipper</span>
  </div>
</section>

<section class="card card-front" aria-label="Card front">
  <svg class="swoosh" viewBox="0 0 640 366" preserveAspectRatio="none" aria-hidden="true">
    <defs>
      <linearGradient id="orangeBand" x1="0" x2="1">
        <stop offset="0" stop-color="var(--orange-deep)"/>
        <stop offset="1" stop-color="var(--orange)"/>
      </linearGradient>
    </defs>
    <path d="M240 304 C430 298 570 250 640 185 L640 222 C520 278 390 308 240 304Z" fill="var(--slate)"/>
    <path d="M0 262 C170 330 420 305 640 226 L640 366 L0 366Z" fill="url(#orangeBand)" stroke="var(--paper)" stroke-width="4"/>
  </svg>

  <div class="brand">
    <span class="brand-name">Brindle's small</span>
    <span class="brand-line">earthworks and tipper</span>
  </div>

  <div class="contact">
    <p class="contact-name">Your Name</p>
    <p class="contact-title">Job Title</p>
    <p class="contact-row">
      <svg viewBox="0 0 16 16"><path d="M8 1a5 5 0 0 0-5 5c0 4 5 9 5 9s5-5 5-9a5 5 0 0 0-5-5z" fill="var(--orange)"/><circle cx="8" cy="6" r="2" fill="#fff"/></svg>
      Kellerton
    </p>
    <p class="contact-row">
      <svg viewBox="0 0 16 16"><path d="M1 6c0-2 3-3 7-3s7 1 7 3v1h-4V5.5H5V7H1z" fill="var(--orange)"/><rect x="3" y="8" width="10" height="6" rx="1" fill="var(--orange)"/><circle cx="8" cy="11" r="1.6" fill="#fff"/></svg>
      0438571629
    </p>
    <p class="contact-row">
      <svg viewBox="0 0 16 16"><rect x="1" y="3.5" width="14" height="9" fill="var(--orange)"/><path d="M1 3.5l7 5 7-5" fill="none" stroke="#fff" stroke-width="1.3"/></svg>
      brindle.4@fenwickmail.com
    </p>
    <p class="contact-abn"><span>ABN:</span> 62194038715</p>
  </div>
</section>

</body>
</html>
```